Merry Fern Lumo alcohol cooler

I need a design using my Merry Fern Beverage Logo for 4 different styles of Malt Beverage. The cocktails are easy drinking tropical feel. We will be using the best ingredients and try to be all natural and organic.
Zaller Lime
Zaller Orange
Zaller Grapefruit
Zaller Strawberry
We would like as few colors as possible in the design.

Target Market(s)

21 - 50
Women

Requirements
Must have
• the 4 styles
• my LOGO
• label dimension inside 3"wide x 4"high maximum
• 4 pack design
• label must have 12 FL OZ
• label must have 5% ALC/VOL
Nice to have
• Clean crisp feel
Should not have
• please keep design to 3 colors or less

```html
<!DOCTYPE html>
<html lang="en">
<head>
<meta charset="utf-8">
<title>Zaller Malt Beverage Labels</title>
<link rel="stylesheet" href="https://fonts.googleapis.com/css2?family=Abril+Fatface&family=Libre+Baskerville:wght@700&family=Fredoka:wght@600&display=swap">
<style>
  :root {
    --ink: #141414;
    --green: #2d5d47;
    --gold: #c99a4e;
    --paper: #fbfaf6;
    --backdrop: #ececec;
  }
  * { box-sizing: border-box; margin: 0; padding: 0; }
  html, body {
    width: 1200px;
    height: 1000px;
    overflow: hidden;
    background: var(--backdrop);
  }
  .label-sheet {
    width: 1200px;
    height: 1000px;
    display: flex;
    justify-content: center;
    align-items: center;
    gap: 40px;
  }
  .label {
    position: relative;
    width: 250px;
    height: 333px;
    text-align: center;
  }
  .label-shape {
    position: absolute;
    inset: 0;
    width: 250px;
    height: 333px;
  }
  .brand-mark {
    position: absolute;
    top: 40px;
    left: 0;
    right: 0;
    display: flex;
    justify-content: center;
    align-items: center;
    gap: 6px;
    font-family: "Libre Baskerville", Georgia, serif;
    font-weight: 700;
    font-size: 10px;
    letter-spacing: 0.5px;
    text-transform: uppercase;
    color: var(--green);
  }
  .brand-dot {
    width: 12px;
    height: 12px;
    border-radius: 50%;
    background: var(--green);
  }
  .product-name {
    position: absolute;
    top: 64px;
    left: 0;
    right: 0;
    font-family: "Abril Fatface", Georgia, serif;
    font-size: 46px;
    line-height: 1;
    letter-spacing: 1px;
    color: var(--ink);
  }
  .flavor-name {
    position: absolute;
    top: 120px;
    left: 0;
    right: 0;
    font-family: "Libre Baskerville", Georgia, serif;
    font-weight: 700;
    font-size: 17px;
    letter-spacing: 1px;
    color: var(--ink);
  }
  .bottle-art {
    position: absolute;
    top: 156px;
    left: 105px;
    width: 40px;
    height: 36px;
    border-radius: 6px 6px 2px 2px;
    background: var(--green);
  }
  .beverage-type {
    position: absolute;
    top: 232px;
    left: 0;
    right: 0;
    font-family: "Fredoka", "Arial Rounded MT Bold", sans-serif;
    font-weight: 600;
    font-size: 17px;
    color: var(--green);
  }
  .volume, .strength {
    position: absolute;
    left: 0;
    right: 0;
    font-family: "Libre Baskerville", Georgia, serif;
    font-weight: 700;
    font-size: 9px;
    letter-spacing: 0.5px;
    color: var(--ink);
  }
  .volume { top: 276px; }
  .strength { top: 290px; }
</style>
</head>
<body>
<main class="label-sheet">

  <section class="label">
    <svg class="label-shape" viewBox="0 0 250 333" aria-hidden="true">
      <path d="M0 62 L42 18 L208 18 L250 62 L250 305 Q125 345 0 305 Z" fill="var(--paper)"/>
      <path d="M14 250 L14 66 L50 30 L200 30 L236 66 L236 250" fill="none" stroke="var(--gold)" stroke-width="3"/>
      <path d="M14 226 Q125 272 236 226 L236 248 Q125 296 14 248 Z" fill="var(--gold)"/>
    </svg>
    <div class="brand-mark"><span class="brand-dot"></span>Merry Fern Beverage</div>
    <h2 class="product-name">ZALLER</h2>
    <p class="flavor-name">STRAWBERRY</p>
    <div class="bottle-art" role="img" aria-label="Small green bottles illustration"></div>
    <p class="beverage-type">malt beverage</p>
    <p class="volume">12 FL OZ</p>
    <p class="strength">5% ALC/VOL</p>
  </section>

  <section class="label">
    <svg class="label-shape" viewBox="0 0 250 333" aria-hidden="true">
      <path d="M0 62 L42 18 L208 18 L250 62 L250 305 Q125 345 0 305 Z" fill="var(--paper)"/>
      <path d="M14 250 L14 66 L50 30 L200 30 L236 66 L236 250" fill="none" stroke="var(--gold)" stroke-width="3"/>
      <path d="M14 226 Q125 272 236 226 L236 248 Q125 296 14 248 Z" fill="var(--gold)"/>
    </svg>
    <div class="brand-mark"><span class="brand-dot"></span>Merry Fern Beverage</div>
    <h2 class="product-name">ZALLER</h2>
    <p class="flavor-name">GRAPEFRUIT</p>
    <div class="bottle-art" role="img" aria-label="Small green bottles illustration"></div>
    <p class="beverage-type">malt beverage</p>
    <p class="volume">12 FL OZ</p>
    <p class="strength">5% ALC/VOL</p>
  </section>

  <section class="label">
    <svg class="label-shape" viewBox="0 0 250 333" aria-hidden="true">
      <path d="M0 62 L42 18 L208 18 L250 62 L250 305 Q125 345 0 305 Z" fill="var(--paper)"/>
      <path d="M14 250 L14 66 L50 30 L200 30 L236 66 L236 250" fill="none" stroke="var(--gold)" stroke-width="3"/>
      <path d="M14 226 Q125 272 236 226 L236 248 Q125 296 14 248 Z" fill="var(--gold)"/>
    </svg>
    <div class="brand-mark"><span class="brand-dot"></span>Merry Fern Beverage</div>
    <h2 class="product-name">ZALLER</h2>
    <p class="flavor-name">ORANGE</p>
    <div class="bottle-art" role="img" aria-label="Small green bottles illustration"></div>
    <p class="beverage-type">malt beverage</p>
    <p class="volume">12 FL OZ</p>
    <p class="strength">5% ALC/VOL</p>
  </section>

  <section class="label">
    <svg class="label-shape" viewBox="0 0 250 333" aria-hidden="true">
      <path d="M0 62 L42 18 L208 18 L250 62 L250 305 Q125 345 0 305 Z" fill="var(--paper)"/>
      <path d="M14 250 L14 66 L50 30 L200 30 L236 66 L236 250" fill="none" stroke="var(--gold)" stroke-width="3"/>
      <path d="M14 226 Q125 272 236 226 L236 248 Q125 296 14 248 Z" fill="var(--gold)"/>
    </svg>
    <div class="brand-mark"><span class="brand-dot"></span>Merry Fern Beverage</div>
    <h2 class="product-name">ZALLER</h2>
    <p class="flavor-name">LIME</p>
    <div class="bottle-art" role="img" aria-label="Small green bottles illustration"></div>
    <p class="beverage-type">malt beverage</p>
    <p class="volume">12 FL OZ</p>
    <p class="strength">5% ALC/VOL</p>
  </section>

</main>
</body>
</html>
```